Mezzanine Floor Manufacturer looking for a new business card design

We manufacture mezzanine floors and are providers of racking systems. We provide a range of items/services - simple rack repairs , full warehouse fit outs , manufacturer and install mezzanine floors , partitioning and large turnkey projects. Recently had a new website - www.corvane-shelving.co.uk and would like our business cards updating aswell . Our current card is single sided in the old logo colours (pdf attached) and needs updating.

Target Market(s)

We deal with large projects/ multi national companies and also smaller projects and companies throughout the UK ranging from a single warehouse to a large multi site company.

Industry/Entity Type

Business

Contact Information for Business Card

Will have job title,tel no's, email ,website address etc like example pdf

Requirements
Must have
• Hi - needs to use the colours of the logo & new website. Card needs to be professional

```html
<!DOCTYPE html>
<html lang="en">
<head>
<meta charset="utf-8">
<title>Corvane – Business Card</title>
<link href="https://fonts.googleapis.com/css2?family=Open+Sans:wght@400;600;700&display=swap" rel="stylesheet">
<style>
  :root {
    --page: #e9e6e1;
    --red: #d9232e;
    --red-dark: #b51821;
    --silver-light: #f4f4f4;
    --silver: #d6d6d6;
    --grey-text: #555555;
    --black: #1c1c1c;
    --black-light: #333333;
    --white: #ffffff;
  }
  * { margin: 0; padding: 0; box-sizing: border-box; }
  html, body {
    width: 1200px; height: 1023px; overflow: hidden;
    background: var(--page);
    font-family: "Open Sans", Arial, sans-serif;
  }
  .canvas { position: relative; width: 1200px; height: 1023px; }
  .card {
    position: absolute; width: 540px; height: 309px; overflow: hidden;
    border-radius: 4px;
    box-shadow: 0 6px 18px rgba(0,0,0,.18);
  }
  /* Front */
  .card-front { left: 90px; top: 130px;
    background: linear-gradient(135deg, var(--silver-light), var(--silver)); }
  .front-shape { position: absolute; inset: 0; }
  .brand {
    position: absolute; left: 34px; top: 92px;
    display: flex; align-items: center; gap: 10px;
  }
  .brand-dot { width: 16px; height: 16px; border-radius: 50%; background: var(--red); }
  .brand-name { font-size: 34px; font-weight: 700; color: var(--red); letter-spacing: 1px; }
  .person { position: absolute; right: 34px; top: 26px; text-align: left; width: 220px; }
  .person-name { font-size: 20px; font-weight: 700; color: var(--red); letter-spacing: .5px; }
  .person-title, .person-mobile { font-size: 12px; color: var(--grey-text); letter-spacing: .5px; line-height: 1.5; }
  .address {
    position: absolute; left: 34px; bottom: 26px;
    color: var(--white); font-size: 12px; font-weight: 700; line-height: 1.75;
    text-transform: uppercase; letter-spacing: .4px;
  }
  .contact {
    position: absolute; right: 30px; top: 140px;
    color: var(--white); font-size: 12.5px; font-weight: 700; line-height: 1.75; text-align: right;
  }
  .contact .gap { height: 10px; }
  /* Back */
  .card-back { left: 570px; top: 570px;
    background: repeating-linear-gradient(90deg, var(--black) 0 2px, var(--black-light) 2px 3px); }
  .back-brand {
    position: absolute; left: 0; right: 0; top: 88px; text-align: center;
    font-size: 52px; font-weight: 700; color: var(--red); letter-spacing: 2px;
  }
  .services {
    position: absolute; left: 24px; right: 24px; bottom: 26px;
    color: var(--white); font-size: 10.5px; font-weight: 700; letter-spacing: .5px;
    line-height: 1.9; text-transform: uppercase;
  }
  .services .sep { color: var(--red); margin: 0 5px; }
</style>
</head>
<body>
<main class="canvas">
  <section class="card card-front">
    <svg class="front-shape" width="540" height="309" viewBox="0 0 540 309">
      <defs>
        <linearGradient id="redFill" x1="0" y1="0" x2="1" y2="1">
          <stop offset="0" stop-color="#e8333d"/>
          <stop offset="1" stop-color="#b51821"/>
        </linearGradient>
      </defs>
      <path d="M0 198 C170 178 320 130 540 92 L540 309 L0 309 Z" fill="#9a9a9a"/>
      <path d="M0 208 C170 188 320 140 540 102 L540 309 L0 309 Z" fill="url(#redFill)"/>
    </svg>
    <div class="brand"><span class="brand-dot"></span><span class="brand-name">CORVANE</span></div>
    <div class="person">
      <p class="person-name">DANIEL MARSH</p>
      <p class="person-title">TECHNICAL SALES</p>
      <p class="person-mobile">07700 900417</p>
    </div>
    <address class="address">
      <p>Ashby Mill Lane</p>
      <p>Fenwick Trade Park</p>
      <p>Ashbourne, Derbyshire DE6 1QX</p>
    </address>
    <div class="contact">
      <p>01632 960481</p>
      <p>01632 960592</p>
      <div class="gap"></div>
      <p>dan@corvane-shelving.co.uk</p>
      <p>www.corvane-shelving.co.uk</p>
    </div>
  </section>

  <section class="card card-back">
    <p class="back-brand">CORVANE</p>
    <div class="services">
      <p>Mezzanine Floors<span class="sep">•</span>Cantilever Racking<span class="sep">•</span>Pallet Racking<span class="sep">•</span>Safety Barriers</p>
      <p>Longspan Shelving<span class="sep">•</span>Steel Shelving<span class="sep">•</span>Partitioning<span class="sep">•</span>Turnkey Projects</p>
    </div>
  </section>
</main>
</body>
</html>
```